Business card design needed

I need a business card design for a dog walking, dog minding and dog training business. Please refer to my website for the basic company colours and fonts I'm after. Planning on a double sided card, so all information doesn't need to be on the 'front' side.
Cheers

Industry/Entity Type

Dog Training

Contact Information for Business Card

Meadow Paws - happy hounds
Rua 0498307164
meadowpawsdemo.com.au
-walking
-holiday stays
-onsite care
-training and behavioural consultations

```html
<!DOCTYPE html>
<html lang="en">
<head>
<meta charset="utf-8">
<title>Meadow Paws – business card</title>
<link rel="stylesheet" href="https://fonts.googleapis.com/css2?family=Arimo:wght@400;700&display=swap">
<style>
  :root {
    --orange: #d35220;
    --grey-text: #6a6a6a;
    --card-top: #e9eaea;
    --card-bottom: #ffffff;
    --page: #ffffff;
    --label: #222222;
    --walk-grass: #9a9a6e;
    --walk-path: #cfc8bf;
    --pup-light: #f1eeeb;
    --pup-tone: #d6b89c;
  }
  * { box-sizing: border-box; margin: 0; padding: 0; }
  html, body {
    width: 1143px; height: 1200px; overflow: hidden;
    background: var(--page);
    font-family: "Arimo", Arial, sans-serif;
  }
  .sheet { position: relative; width: 1143px; height: 1200px; }

  .side-label {
    position: absolute; left: 112px;
    font-size: 30px; color: var(--label);
  }
  .side-label--front { top: 150px; }
  .side-label--back { top: 650px; }

  .card {
    position: absolute; left: 175px; width: 790px; height: 441px;
    border-radius: 32px; overflow: hidden;
    background: linear-gradient(to bottom, var(--card-top) 0, var(--card-bottom) 160px);
    box-shadow: 0 6px 10px rgba(0,0,0,.35), 0 0 14px rgba(0,0,0,.2);
  }
  .card--front { top: 128px; }
  .card--back { top: 610px; background: linear-gradient(to bottom, var(--card-top) 0, var(--card-bottom) 150px); }

  .brand-name {
    position: absolute; left: 0; right: 0; text-align: center;
    font-weight: 700; color: var(--orange); letter-spacing: 1px;
  }
  .card--front .brand-name { top: 50px; font-size: 56px; }
  .card--back .brand-name { top: 62px; left: 0; width: 794px; font-size: 48px; }

  .band {
    position: absolute; left: 0; right: 0; height: 52px;
    background: var(--orange); color: #fff; font-weight: 700;
    display: flex; align-items: center; justify-content: center;
  }
  .card--front .band { top: 159px; font-size: 30px; }
  .card--back .band { top: 164px; font-size: 27px; }

  .photo-walk {
    position: absolute; left: 0; right: 0; top: 211px; bottom: 0;
    background: linear-gradient(to bottom, var(--walk-grass) 0%, var(--walk-path) 55%, #bdb3a8 100%);
  }
  .photo-pup {
    position: absolute; right: 6px; top: 6px; width: 216px; height: 142px;
    background: radial-gradient(ellipse at 55% 45%, var(--pup-tone) 0%, var(--pup-light) 55%, rgba(241,238,235,0) 80%);
  }

  .contact {
    position: absolute; top: 254px; left: 0; right: 0;
    display: flex; flex-direction: column; align-items: center; gap: 8px;
    font-size: 25px; font-weight: 700; color: var(--grey-text);
  }
  .contact__row { display: flex; align-items: center; gap: 10px; }
  .contact__icon { width: 24px; height: 24px; flex: none; }
  .contact__row--mail { margin-left: -8px; }

  .services {
    position: absolute; top: 350px; left: 0; right: 0; text-align: center;
    font-size: 25px; line-height: 32px; color: var(--grey-text);
  }
  .services__dot { color: var(--orange); font-size: 20px; vertical-align: 2px; margin: 0 4px; }
</style>
</head>
<body>
<div class="sheet">
  <span class="side-label side-label--front">1</span>
  <section class="card card--front">
    <div class="brand-name">Meadow Paws</div>
    <div class="band">www.meadowpawsdemo.com.au</div>
    <div class="photo-walk" role="img" aria-label="Photo of a group of dogs being walked on leads along a garden path"></div>
  </section>

  <span class="side-label side-label--back">2</span>
  <section class="card card--back">
    <div class="brand-name">Meadow Paws</div>
    <div class="photo-pup" role="img" aria-label="Photo of a puppy peeking over a ledge"></div>
    <div class="band">happy hounds</div>
    <div class="contact">
      <div class="contact__row">
        <svg class="contact__icon" viewBox="0 0 24 24" aria-hidden="true">
          <path d="M6.5 3.5c.8-.4 1.6 0 2 .8l1.4 2.8c.3.7.1 1.5-.5 1.9l-1.3.9c.9 2.3 2.6 4.3 4.8 5.6l1-1.2c.5-.6 1.3-.7 2-.3l2.7 1.6c.7.4 1 1.3.6 2l-.7 1.3c-.6 1.1-1.9 1.6-3.1 1.2C9.8 18.5 5.3 13.7 4 7.9c-.3-1.2.2-2.4 1.3-3z" fill="var(--orange)"/>
        </svg>
        <span>Rua 0498307164</span>
      </div>
      <div class="contact__row contact__row--mail">
        <svg class="contact__icon" viewBox="0 0 24 24" aria-hidden="true">
          <rect x="2.5" y="5.5" width="19" height="13" fill="none" stroke="var(--orange)" stroke-width="1.6"/>
          <path d="M2.5 5.5l9.5 7.5 9.5-7.5M2.5 18.5l7-6M21.5 18.5l-7-6" fill="none" stroke="var(--orange)" stroke-width="1.6"/>
        </svg>
        <span>hello@meadowpawsdemo.com.au</span>
      </div>
    </div>
    <div class="services">
      walking <span class="services__dot">●</span> holiday stays <span class="services__dot">●</span> onsite care<br>
      training and behavioural consultations
    </div>
  </section>
</div>
</body>
</html>
```